High End Business Card Design for Flooring Store

Looking for a new card design for our hardwood flooring company. We have no print budget for these and are open to cards made from wood, metal, cardstock with embossed print ... or any combination of these. No plastic.

We sell luxury products and I want the cards to reflect our image of quality and class.

Our contact information as such;
Employee Name
418 Colbrook Blvd.
Brenton, ON
K9R-3M5
(555) 214-3968
Employee email @velkaflooring.com

Target Market(s)

Home Builders

Contact Information for Business Card

Emnployee name, business contact information

```html
<!DOCTYPE html>
<html lang="en">
<head>
<meta charset="utf-8">
<title>Velka Flooring – Business Card</title>
<link rel="stylesheet" href="https://fonts.googleapis.com/css2?family=Mulish:wght@400;500&display=swap">
<style>
  :root {
    --stage: #2b2b2b;
    --card-dark: #262627;
    --card-dark-lift: #38393b;
    --card-light: #efefef;
    --brand-red: #9b2a22;
    --brand-gold: #e6b02a;
    --text-gray: #6a6a6a;
    --tag-gray: #5c5c5c;
  }
  * { box-sizing: border-box; margin: 0; padding: 0; }
  html, body {
    width: 1079px;
    height: 1200px;
    overflow: hidden;
    background: var(--stage);
    font-family: "Mulish", sans-serif;
  }
  .sheet {
    width: 1079px;
    height: 1200px;
    display: flex;
    flex-direction: column;
    align-items: center;
    justify-content: center;
    gap: 40px;
  }
  .card {
    position: relative;
    width: 820px;
    height: 522px;
    border-radius: 30px;
    overflow: hidden;
    box-shadow: 0 14px 30px rgba(0,0,0,0.45);
  }
  .card--back { background: var(--card-dark); }
  .card--back svg { display: block; width: 100%; height: 100%; }
  .back-name {
    font-family: "Mulish", sans-serif;
    font-weight: 500;
    font-size: 118px;
    fill: var(--brand-red);
  }
  .back-tagline {
    font-family: "Mulish", sans-serif;
    font-weight: 400;
    font-size: 31px;
    fill: var(--tag-gray);
  }

  .card--front { background: var(--card-light); }
  .brand-block {
    position: absolute;
    left: 42px;
    top: 175px;
    width: 320px;
    text-align: center;
  }
  .brand-name {
    display: flex;
    align-items: center;
    justify-content: center;
    gap: 10px;
    color: var(--brand-red);
    font-size: 74px;
    font-weight: 500;
    line-height: 1;
  }
  .brand-square {
    width: 30px;
    height: 30px;
    background: var(--brand-gold);
  }
  .brand-tagline {
    margin-top: 4px;
    color: var(--text-gray);
    font-size: 19px;
    line-height: 1.1;
  }
  .divider {
    position: absolute;
    left: 394px;
    top: 108px;
    width: 2px;
    height: 278px;
    background: var(--brand-red);
  }
  .person {
    position: absolute;
    left: 460px;
    top: 118px;
  }
  .person-name {
    color: var(--brand-red);
    font-size: 41px;
    font-weight: 500;
    line-height: 1.1;
  }
  .person-role {
    color: var(--text-gray);
    font-size: 27px;
    font-weight: 400;
    line-height: 1.3;
  }
  .contacts {
    position: absolute;
    left: 444px;
    top: 250px;
    list-style: none;
  }
  .contacts li {
    display: flex;
    align-items: center;
    gap: 10px;
    color: var(--text-gray);
    font-size: 25px;
    line-height: 37px;
  }
  .contacts svg { width: 24px; height: 24px; flex: none; }
  .address {
    position: absolute;
    left: 0;
    right: 0;
    top: 426px;
    text-align: center;
    color: var(--brand-red);
    font-size: 27px;
  }
</style>
</head>
<body>
<main class="sheet">

  <section class="card card--back" aria-label="Card back">
    <svg viewBox="0 0 820 522" xmlns="http://www.w3.org/2000/svg">
      <defs>
        <linearGradient id="backShade" x1="0" y1="0" x2="1" y2="1">
          <stop offset="0" stop-color="var(--card-dark-lift)"/>
          <stop offset="0.55" stop-color="var(--card-dark)"/>
          <stop offset="1" stop-color="#1c1c1d"/>
        </linearGradient>
      </defs>
      <rect class="card-ground" width="820" height="522" fill="url(#backShade)"/>
      <g transform="translate(420,100) rotate(40)">
        <text class="back-name" x="0" y="0">Velka</text>
        <text class="back-tagline" x="8" y="42">Planchers &amp; Escaliers</text>
        <text class="back-tagline" x="8" y="78">Flooring &amp; Stairs</text>
      </g>
    </svg>
  </section>

  <section class="card card--front" aria-label="Card front">
    <div class="brand-block">
      <div class="brand-name"><span class="brand-square"></span>Velka</div>
      <p class="brand-tagline">Planchers &amp; Escaliers<br>Flooring &amp; Stairs</p>
    </div>

    <div class="divider"></div>

    <div class="person">
      <h1 class="person-name">Employee NAME</h1>
      <p class="person-role">Function</p>
    </div>

    <ul class="contacts">
      <li>
        <svg viewBox="0 0 24 24" aria-hidden="true"><path fill="var(--brand-red)" d="M6.6 10.8a15.1 15.1 0 0 0 6.6 6.6l2.2-2.2c.3-.3.7-.4 1-.2 1.1.4 2.3.6 3.6.6.6 0 1 .4 1 1V20c0 .6-.4 1-1 1C10.6 21 3 13.4 3 4c0-.6.4-1 1-1h3.5c.6 0 1 .4 1 1 0 1.3.2 2.5.6 3.6.1.3 0 .7-.2 1z"/><path fill="none" stroke="var(--brand-red)" stroke-width="1.8" d="M14 3.5a6.5 6.5 0 0 1 6.5 6.5M14 7a3 3 0 0 1 3 3"/></svg>
        (555) 214-3968
      </li>
      <li>
        <svg viewBox="0 0 24 24" aria-hidden="true"><rect x="2" y="5" width="20" height="14" fill="var(--brand-red)"/><path d="M2 5l10 8 10-8M2 19l7-7M22 19l-7-7" fill="none" stroke="var(--card-light)" stroke-width="1.5"/></svg>
        email@velkaflooring.com
      </li>
      <li>
        <svg viewBox="0 0 24 24" aria-hidden="true"><g fill="none" stroke="var(--brand-red)" stroke-width="2"><circle cx="12" cy="12" r="9"/><ellipse cx="12" cy="12" rx="4" ry="9"/><path d="M3 12h18M5 7h14M5 17h14"/></g></svg>
        velkaflooring.com
      </li>
    </ul>

    <p class="address">418 Colbrook Blvd. Brenton, ON - K9R-3M5</p>
  </section>

</main>
</body>
</html>
```